Modern, Funky, High-End Coffee Packaging Design

We are a coffee roaster that is wanting to redesign our bags so they look more professional, yet modern, funky & fun. The design would need to stand up to other national coffee roasters like Lantern Ridge, Brightmoor, or other high-end specialty coffee roasters.

Sunny-Crate is a social enterprise (a for-profit supporting a non-profit). We buy directly from our farmers in Nicaragua so they receive better wages and then we give back a portion of our profits to Open Harvest Outreach Nicaragua www.openharvestout.org We named the company Sunny-Crate off the idea of "Well-Being" so we like to portray health, wellness, and balance (which is why our coffee bean in our logo looks a bit like the yin yang symbol). We really like the idea behind the 7 Chakras (as far as the colors & the wellness themes since we have 7 coffees). This may be nice to incorporate into the bag design.

We sell our coffees in 12 oz and 2.2 pound bags. Bag dimensions templates are attached for the 2.2 pound bags. We have chosen “white matte with metallic effects” bag so the design should reflect the matte white color.

We like the "flavor wheel" idea we have on our current labels. We have included photos of current Kraft brown coffee bags AND an .ai file of one of the labels. We have a total of 7 coffees. We are awarding the best design for one label to make sure we find a fit. If we like the design we would pay an additional amount for the other 6 designs. We have included an example design of a white 2.2 pound bag. This is the bag we will use but not the design. We want to utilize all parts of the bag in the design (like the example we have provided).

The labels will need the following:

Front:
1) Logo
2) Name of Coffee (we would like helping naming them maybe after the wellness theme)
3) Roast type (light, medium, or dark)
4) The flavor wheel with custom (modern, funky design)
5) 12 oz or 2.2 lbs based on the bag you are designing
6) Include "100% specialty grade, arabica coffee'
7) Say "Small batch roasted"

Back: Info about Sunny-Crate (feel free to look at our website if you want to know more about our company sunny-crate.com )

1) Name: Sunny-Crate Coffee Roasters
2) Address: 2871 Dorrington Pike Ave suite 214
Wake Forest, NC 27587
3) 1-833-555-CRAT
4) Website: www.Sunny-Crate.com
5) Barcode (this can also be on the bottom of the bag)
6) Roast date (with a white blank area for us to stamp roast date)
7) Our logo
8) other information about Sunny-Crate

Side #1: "Poured for Good"
Information about Open Harvest and how Sunny-Crate financially supports Open Harvest and their wellness initiatives in rural northwest Nicaragua. Sunny-Crate's owner Karina Tolliver's parents' started Open Harvest in 2002 and Karina has visited every year since. She started sourcing coffee from Nicaragua in 2012 to support their mission and Sunny-Crate was born. I have uploaded pics and a logo from Open Harvest.
*We have attached photos of the children we work with in the mission if you would like to incorporate the photos on the bag design. We own the rights to the photos.

Side #2: "Direct Trade Initiative" Info about working with the Farmers in Nicaragua and sourcing directly from them so they receive better wages. Sunny-Crate's goal is to source 100% of their coffee beans direct from all farming partners by 2022. Currently we work with Finca de Las Lomas in Matagalpa, Nicaragua. The farm owners are Teodoro & Ernesto Quintal.
*I have uploaded several pics from the farm and of the coffee beans.
*We have included several pictures of the farm, photos with the owner Karina & the farmers, and photos of the coffee cherries at the farm. Feel free to use any of the photos in your design.

Target Market(s)

25-55

Colors
acd136
0592cd
f04a50
b768aa
e34197
f78f20
00a990

Requirements
Must have
• Design that will look good on a white, matte foil bag with metallic effects. The design should be modern, funky, with a high-end feel, yet playful. We like the colors we chose from the color wheel in the design description but don't feel like you have to use all of them.
Nice to have
• A bag design that will pop and stand out on grocery store shelves.

```html
<!DOCTYPE html>
<html lang="en">
<head>
<meta charset="utf-8">
<title>Sunny-Crate Brazil Medium – 2.2 lbs bag</title>
<link href="https://fonts.googleapis.com/css2?family=Josefin+Sans:wght@400;600;700&family=Oswald:wght@600&family=Lexend:wght@700&display=swap" rel="stylesheet">
<style>
  :root{
    --stage:#0050a4;
    --white:#ffffff;
    --ink:#2f4a5c;
    --navy:#1f2f45;
    --red:#f0412f;
    --orange:#f78f20;
    --gold:#f5b323;
    --blue:#0592cd;
    --teal:#00a990;
    --grey:#b9c0c6;
  }
  *{margin:0;padding:0;box-sizing:border-box}
  html,body{width:1200px;height:960px;overflow:hidden;background:var(--stage)}
  .stage{position:relative;width:1200px;height:960px;display:flex;align-items:center;justify-content:center}
  .panel{position:relative;height:780px}
  .side-gusset{width:170px;background:linear-gradient(90deg,#e9ecef,#ffffff 45%,#f3f4f6)}
  .front{width:440px;background:var(--white)}
  .front svg{position:absolute;inset:0;width:100%;height:100%}
  .brand{position:absolute;left:0;right:0;display:flex;align-items:center;justify-content:center;gap:10px;font-family:"Josefin Sans",sans-serif;font-weight:700;color:var(--navy);line-height:1}
  .brand i{display:inline-block;border-radius:50%;background:var(--navy)}
  .front .brand{top:96px;font-size:34px}
  .front .brand i{width:18px;height:18px}
  .side-gusset .brand{top:580px;font-size:20px;gap:6px}
  .side-gusset .brand i{width:11px;height:11px}
  .flavor{position:absolute;font-family:"Josefin Sans",sans-serif;font-weight:600;font-size:15px;letter-spacing:1px;color:var(--ink)}
  .flavor.toasty{left:40px;top:348px;transform:rotate(42deg)}
  .flavor.fruity{right:40px;top:348px;transform:rotate(-42deg)}
  .title{position:absolute;left:0;right:0;top:418px;text-align:center;color:var(--ink)}
  .title h1{font-family:"Lexend",sans-serif;font-weight:700;font-size:58px;letter-spacing:3px;line-height:1}
  .title .roast{font-family:"Oswald",sans-serif;font-size:28px;color:var(--navy);margin-top:8px;letter-spacing:1px}
  .title .roast span{font-size:14px;margin:0 6px;vertical-align:middle}
  .title .grade{font-family:"Josefin Sans",sans-serif;font-weight:600;font-size:12px;letter-spacing:1.5px;line-height:1.9;margin-top:14px}
  .weight{position:absolute;left:0;right:0;top:680px;text-align:center;font-family:"Oswald",sans-serif;color:var(--navy);line-height:1}
  .weight b{display:block;font-size:26px}
  .weight small{display:block;font-size:15px;margin-top:3px}
  .side-name{position:absolute;left:50%;top:250px;transform:translateX(-50%) rotate(-90deg);font-family:"Lexend",sans-serif;font-weight:700;font-size:70px;letter-spacing:4px;color:var(--white);text-shadow:0 0 2px var(--grey)}
  .fine-print{position:absolute;left:18px;right:18px;top:630px;font-family:"Josefin Sans",sans-serif;font-size:7px;line-height:1.4;color:var(--navy)}
</style>
</head>
<body>
<main class="stage">
  <section class="panel side-gusset">
    <div class="side-name">BRAZIL</div>
    <div class="brand"><i></i>Sunny-Crate</div>
    <p class="fine-print">Our coffee is small batch roasted with care. Every bag supports fair wages for the farmers who grow it.</p>
  </section>

  <section class="panel front">
    <svg viewBox="0 0 440 780" preserveAspectRatio="none">
      <defs>
        <linearGradient id="pattern-tones" x1="0" y1="0" x2="1" y2="1">
          <stop offset="0" stop-color="#f0412f"/>
          <stop offset="0.3" stop-color="#f5b323"/>
          <stop offset="0.55" stop-color="#0592cd"/>
          <stop offset="0.75" stop-color="#00a990"/>
          <stop offset="1" stop-color="#1f2f45"/>
        </linearGradient>
      </defs>
      <rect class="pattern-field" width="440" height="780" fill="url(#pattern-tones)" role="img" aria-label="Geometric triangle pattern in red, gold, blue, teal and navy"/>
      <polygon class="top-field" points="0,0 440,0 440,150 220,290 0,150" fill="#ffffff"/>
      <polygon class="flavor-band" points="0,230 50,230 210,390 160,440 0,300" fill="#ffffff"/>
      <polygon class="flavor-band" points="440,230 390,230 230,390 280,440 440,300" fill="#ffffff"/>
      <polygon class="name-diamond" points="220,340 420,490 220,650 20,490" fill="#ffffff"/>
      <polygon class="weight-diamond" points="220,648 268,708 220,768 172,708" fill="#ffffff"/>
      <polygon points="220,610 236,626 220,642 204,626" fill="#f0412f"/>
    </svg>
    <div class="brand"><i></i>Sunny-Crate</div>
    <span class="flavor toasty">TOASTY</span>
    <span class="flavor fruity">FRUITY</span>
    <div class="title">
      <h1>BRAZIL</h1>
      <p class="roast"><span>✱</span>MEDIUM<span>✱</span></p>
      <p class="grade">100% SPECIALTY GRADE,<br>ARABICA COFFEE</p>
    </div>
    <div class="weight"><b>2.2</b><small>LBS</small></div>
  </section>
</main>
</body>
</html>
```